Shipping container company needs 7 print ads developed

We sell and rent shipping containers as affordable storage solutions.Target markets are agricultural, construction, commercial, warehouse, manufacturing, and hobby farms. I need seven persona -specific (see attached 7 personas) clean minimalistic 4.375" x 4" ads in color with graphics, copy, 20' stock container image, and logo. Also, see attached brand guidelines.. Special note -phone number needs to be changed to 555.014.3829

```html
<!DOCTYPE html>
<html lang="en">
<head>
<meta charset="utf-8">
<title>Ridgeline Containers – Print Ad Samples</title>
<link rel="stylesheet" href="https://fonts.googleapis.com/css2?family=Montserrat:wght@400;500;600;700;800&display=swap">
<style>
  :root {
    --page-bg: #b4b4b4;
    --label: #7d7474;
    --navy: #16233a;
    --navy-deep: #0f1a2c;
    --teal: #2fbfa6;
    --white: #ffffff;
    --ink: #1b2638;
    --sky-top: #e9f1f8;
    --sky-mid: #bcd3e8;
    --rust: #c45a34;
    --red: #c8353a;
    --storm: #3a4350;
  }
  * { box-sizing: border-box; margin: 0; padding: 0; }
  html, body { width: 1200px; height: 2500px; overflow: hidden; }
  body {
    background: var(--page-bg);
    font-family: "Montserrat", Arial, sans-serif;
    position: relative;
  }
  .sample-label {
    position: absolute; left: 0; width: 1200px; text-align: center;
    font-weight: 700; font-size: 24px; letter-spacing: 1px; color: var(--label);
  }
  .ad {
    position: absolute; left: 272px; width: 656px; height: 664px; overflow: hidden;
  }
  .headline {
    font-size: 46px; line-height: 1.08; letter-spacing: -0.5px; font-weight: 400;
  }
  .headline strong { font-weight: 700; display: block; }
  .brand {
    display: flex; align-items: center; gap: 10px;
    font-weight: 600; font-size: 22px; line-height: 1.05; color: var(--navy);
  }
  .brand-square { width: 38px; height: 38px; background: var(--navy); flex: none; }
  .phone { font-weight: 700; }

  /* Sample 1 */
  .ad--sky { top: 108px; background: var(--white); }
  .ad--sky .photo {
    position: absolute; inset: 0 0 60px 0;
    background: linear-gradient(180deg, var(--sky-top) 0%, var(--sky-mid) 30%, #9db6cc 42%, var(--rust) 55%, #4a6b9c 70%, #c9413b 82%, #3f6f57 100%);
  }
  .ad--sky .headline { position: absolute; left: 28px; top: 30px; color: var(--ink); }
  .ad--sky .brand { position: absolute; right: 24px; top: 40px; }
  .ad--sky .contact-bar {
    position: absolute; left: 0; bottom: 0; width: 100%; height: 60px;
    background: var(--white); display: flex; align-items: center; padding-left: 28px;
    font-size: 20px; font-weight: 500; color: var(--ink); gap: 8px;
  }

  /* Samples 2 & 3 shared */
  .ad--storm { background: var(--navy); }
  .ad--storm .photo {
    position: absolute; left: 0; width: 100%;
    background: radial-gradient(ellipse at 50% 60%, var(--red) 0%, #8e2a30 28%, var(--storm) 55%, var(--navy-deep) 100%);
  }
  .ad--storm .headline { position: absolute; left: 0; width: 100%; text-align: center; color: var(--white); }
  .ad--storm .headline strong { color: var(--teal); }

  /* Sample 2 */
  .ad--tab { top: 904px; }
  .ad--tab .photo { top: 250px; height: 370px; }
  .brand-tab {
    position: absolute; left: 200px; top: 0; width: 256px; height: 88px;
    background: var(--white); display: flex; align-items: center; justify-content: center;
    clip-path: polygon(0 0, 100% 0, 100% 78%, 50% 100%, 0 78%);
  }
  .ad--tab .headline { top: 130px; }
  .ad--tab .contact-line {
    position: absolute; left: 0; bottom: 20px; width: 100%; text-align: center;
    font-size: 20px; font-weight: 500; color: var(--teal);
  }
  .ad--tab .contact-line .phone { color: var(--white); }

  /* Sample 3 */
  .ad--footer { top: 1700px; }
  .ad--footer .headline { top: 50px; font-size: 50px; }
  .ad--footer .photo { top: 170px; height: 390px; }
  .footer-bar {
    position: absolute; left: 0; bottom: 0; width: 100%; height: 104px;
    background: var(--white); display: flex; align-items: center; padding: 0 24px;
  }
  .footer-divider { width: 2px; height: 64px; background: var(--navy); margin: 0 28px 0 40px; }
  .footer-contact { display: flex; flex-direction: column; }
  .footer-contact .lead { font-size: 18px; font-weight: 500; color: var(--teal); }
  .footer-contact .phone { font-size: 40px; color: var(--navy); line-height: 1.05; }
</style>
</head>
<body>

  <div class="sample-label" style="top:58px;">SAMPLE 1</div>
  <section class="ad ad--sky">
    <div class="photo" role="img" aria-label="Stacked colourful shipping containers under a bright sky"></div>
    <h1 class="headline">Trusted containers,<strong>exceptional service.</strong></h1>
    <div class="brand"><span class="brand-square"></span><span>Ridgeline<br>Containers</span></div>
    <div class="contact-bar"><span>Get More Details, Contact us</span><span class="phone">555.014.3829</span></div>
  </section>

  <div class="sample-label" style="top:840px;">SAMPLE 2</div>
  <section class="ad ad--storm ad--tab">
    <div class="photo" role="img" aria-label="Two red shipping containers lifted by cranes against a stormy sky"></div>
    <div class="brand-tab"><div class="brand"><span class="brand-square"></span><span>Ridgeline<br>Containers</span></div></div>
    <h2 class="headline">Trusted containers,<strong>exceptional service.</strong></h2>
    <div class="contact-line">Get More Details, Contact us <span class="phone">555.014.3829</span></div>
  </section>

  <div class="sample-label" style="top:1628px;">SAMPLE 3</div>
  <section class="ad ad--storm ad--footer">
    <h2 class="headline">Trusted containers,<strong>exceptional service.</strong></h2>
    <div class="photo" role="img" aria-label="Two red shipping containers lifted by cranes against a stormy sky"></div>
    <div class="footer-bar">
      <div class="brand"><span class="brand-square"></span><span>Ridgeline<br>Containers</span></div>
      <div class="footer-divider"></div>
      <div class="footer-contact">
        <span class="lead">Get More Details, Contact us</span>
        <span class="phone">555.014.3829</span>
      </div>
    </div>
  </section>

</body>
</html>
```